Kelmora Legal Business Card

I require a corporate business card for a new legal services business.

I do not have a logo, nor do I want one.

I require a clean, neat a professional card for a law firm.

Details:

Business Name: Kelmora Legal
Name: Debra Lindqvist
Title: Corporate Services Manager
Location: Office 14 (Top Floor), Toravel Business Centre, Quinlan Grove Street, Alotau CBD, Milne Bay Province.
Postal Address: PO Box 593, Alotau, 211, Milne Bay Province, Papua New Guinea.
Contact: T: +675 6418250, F: +675 6413362, M: +675 72915867, E: dlindqvist@kelmoraexample.com.pg.

I look forward to your design submissions.

Industry/Entity Type

Legal

```html
<!DOCTYPE html>
<html lang="en">
<head>
<meta charset="utf-8">
<title>Kelmora Legal – Business Card</title>
<link rel="stylesheet" href="https://fonts.googleapis.com/css2?family=Barlow:wght@300;400;500;700&display=swap">
<style>
  :root {
    --page-bg: #e4e6ec;
    --card-bg: #ffffff;
    --ink: #2f3133;
    --ink-soft: #8a8d91;
    --rule-grey: #c9cbce;
    --accent-blue: #3d95c6;
    --band-tint: #dfe6e9;
  }
  * { margin: 0; padding: 0; box-sizing: border-box; }
  html, body {
    width: 1200px; height: 1066px; overflow: hidden;
    background: var(--page-bg);
    font-family: "Barlow", Arial, sans-serif;
    color: var(--ink);
  }
  .business-card {
    position: absolute; left: 150px; top: 273px;
    width: 900px; height: 520px;
    background: var(--card-bg);
    box-shadow: 0 10px 30px rgba(40, 50, 70, 0.18);
    overflow: hidden;
  }
  .firm-name {
    position: absolute; left: 60px; top: 48px;
    font-size: 52px; font-weight: 700; letter-spacing: -0.5px;
    color: var(--ink);
  }
  .header-rule {
    position: absolute; left: 0; top: 128px;
    width: 620px; height: 3px; background: var(--rule-grey);
  }
  .person {
    position: absolute; right: 0; top: 122px;
    width: 280px; padding-left: 12px;
  }
  .person-name { font-size: 34px; font-weight: 700; line-height: 1; }
  .person-title {
    font-size: 17px; font-weight: 300; color: var(--ink-soft);
    margin-top: 4px; padding-bottom: 6px;
    border-bottom: 3px solid var(--accent-blue);
  }
  .address {
    position: absolute; left: 70px; top: 168px;
    font-size: 17px; line-height: 1.35; font-weight: 400;
  }
  .postal {
    position: absolute; left: 70px; top: 268px;
    font-size: 17px; font-weight: 400;
  }
  .contacts {
    position: absolute; left: 70px; top: 318px; right: 40px;
    display: flex; gap: 34px; font-size: 17px;
  }
  .contacts b { font-weight: 700; margin-right: 4px; }
  .footer-band {
    position: absolute; left: 0; bottom: 0;
    width: 100%; height: 100px;
    background: var(--band-tint);
    border-top: 4px solid var(--accent-blue);
  }
</style>
</head>
<body>
  <article class="business-card">
    <div class="firm-name">Kelmora Legal</div>
    <div class="header-rule"></div>
    <div class="person">
      <div class="person-name">Debra Lindqvist</div>
      <div class="person-title">Corporate Services Manager</div>
    </div>
    <p class="address">
      Office 14 (Top Floor)<br>
      Toravel Business Centre<br>
      Quinlan Grove Street, Alotau CBD, Milne Bay Province
    </p>
    <p class="postal">PO Box 593, Alotau, 211, Milne Bay Province, Papua New Guinea</p>
    <div class="contacts">
      <span><b>T:</b>+675 6418250</span>
      <span><b>F:</b>+675 6413362</span>
      <span><b>M:</b>+675 72915867</span>
      <span><b>E:</b>dlindqvist@kelmoraexample.com.pg</span>
    </div>
    <div class="footer-band" role="img" aria-label="Pale diagonal stripe pattern band"></div>
  </article>
</body>
</html>
```